Quiet Ledger needs a book cover

Enabling people to find a new way of looking at money. If peoples thoughts, attitude and emotions around money are not inline with their goals and dreams then it is often harder to achieve their version of success.

Recognition that we have an emotional and a practical way with money.

Quiet Ledger enables people to find a sustainable (balanced) way with money for their life right now and their future.

Developing this over the years and seeing clients achieve a clear picture/idea/thought connection that is positive around money and it's purpose to them in their lives has truly been fabulous as they have then gone on to achieve their goals and dreams.

Title of book = Quiet Ledger
Tag line = Being healthy being wealthy
Authors Name = Ruth Pell
Book Size = 135 width x 185 height
Thumbnail = Cover must work well as well as full size
Looking for simple and clear app-able / icon type image
Feel free to have fun with it
A simple yet refreshing balanced, eye-catching design.

The back will include authors photo, blurb, testimonials, barcode, ISBN number & price. I will provide once front cover is sorted.

Reason: Realised that the tag line for the book was incorrect.

Target Market(s)

Individuals

Industry/Entity Type

Work

Requirements
Must have
• First work on front cover, once approved we can then do spine and back cover

```html
<!DOCTYPE html>
<html lang="en">
<head>
<meta charset="utf-8">
<title>Quiet Ledger – Book Cover</title>
<link rel="stylesheet" href="https://fonts.googleapis.com/css2?family=Abril+Fatface&family=Nunito:wght@800&family=Oxygen:wght@400;700&display=swap">
<style>
  :root {
    --backdrop: #e9e4dd;
    --shirt-light: #e4e4e4;
    --shirt-mid: #d3d3d3;
    --tie-green: #4f9a2c;
    --tie-dark: #2f5f1c;
    --accent-pink: #e62b8c;
    --ink: #1c1c1c;
    --pocket-line: #3a3a3a;
    --flap-top: #f2f2f2;
    --flap-bottom: #dedede;
    --white: #ffffff;
  }
  html, body {
    margin: 0;
    padding: 0;
    width: 1200px;
    height: 1107px;
    overflow: hidden;
    background: var(--backdrop);
  }
  .cover {
    position: absolute;
    left: 225px;
    top: 40px;
    width: 750px;
    height: 1028px;
    background: linear-gradient(180deg, var(--shirt-light), var(--shirt-mid));
    box-shadow: 0 6px 18px rgba(0,0,0,0.25);
    overflow: hidden;
  }
  .cover-shapes {
    position: absolute;
    inset: 0;
  }
  .author-badge {
    position: absolute;
    left: 278px;
    top: 128px;
    width: 334px;
    height: 72px;
    background: var(--accent-pink);
    color: var(--white);
    font-family: "Nunito", sans-serif;
    font-weight: 800;
    font-size: 46px;
    line-height: 72px;
    text-align: center;
  }
  .book-title {
    position: absolute;
    right: 139px;
    top: 236px;
    margin: 0;
    text-align: right;
    font-family: "Abril Fatface", serif;
    font-weight: 400;
    color: var(--accent-pink);
    line-height: 0.9;
  }
  .book-title .title-small { display: block; font-size: 50px; }
  .book-title .title-large { display: block; font-size: 96px; margin-top: -8px; }
  .question {
    position: absolute;
    right: 112px;
    top: 450px;
    margin: 0;
    text-align: right;
    font-family: "Oxygen", sans-serif;
    color: var(--ink);
    font-size: 56px;
    line-height: 1;
  }
  .question span { display: block; }
  .question em {
    font-style: italic;
    font-weight: 700;
    font-size: 72px;
  }
  .question .line-of { margin: -4px 0 -6px; }
  .question .line-in { margin-top: -6px; }
</style>
</head>
<body>
  <main class="cover">
    <svg class="cover-shapes" width="750" height="1028" viewBox="0 0 750 1028">
      <defs>
        <linearGradient id="flapShade" x1="0" y1="0" x2="0" y2="1">
          <stop offset="0" stop-color="var(--flap-top)"/>
          <stop offset="1" stop-color="var(--flap-bottom)"/>
        </linearGradient>
        <linearGradient id="tieShade" x1="0" y1="0" x2="1" y2="0">
          <stop offset="0" stop-color="var(--tie-dark)"/>
          <stop offset="0.5" stop-color="var(--tie-green)"/>
          <stop offset="1" stop-color="var(--tie-dark)"/>
        </linearGradient>
      </defs>
      <polygon class="necktie" role="img" aria-label="Green and navy striped necktie hanging down the shirt front"
               points="0,0 72,0 168,1028 0,1028" fill="url(#tieShade)"/>
      <path class="pocket-body" d="M203 384 H689 V812 Q446 858 203 812 Z"
            fill="none" stroke="var(--pocket-line)" stroke-width="1.5"/>
      <rect class="pocket-flap" x="188" y="224" width="514" height="160" rx="8"
            fill="url(#flapShade)" stroke="var(--pocket-line)" stroke-width="1.5"/>
    </svg>

    <div class="author-badge">Ruth Pell</div>

    <h1 class="book-title">
      <span class="title-small">Quiet</span>
      <span class="title-large">Ledger</span>
    </h1>

    <p class="question">
      <span>What is the</span>
      <span><em>purpose</em></span>
      <span class="line-of">of</span>
      <span><em>money</em></span>
      <span class="line-in">in your</span>
      <span><em>life</em>?</span>
    </p>
  </main>
</body>
</html>
```